PLM - Business Card Design Project

We need a business card based on our logo
Updates

Hi I just upload logo file in AI format Thanks and regards

Target Market(s)

Bank, Big companies, Business owners

Industry/Entity Type

Business

Font styles to use
Sans Serif

```html
<!DOCTYPE html>
<html lang="en">
<head>
<meta charset="utf-8">
<title>PLM Business Card</title>
<link href="https://fonts.googleapis.com/css2?family=Exo+2:wght@400;600&display=swap" rel="stylesheet">
<style>
  :root {
    --navy: #14294b;
    --bar-grey: #c9cacb;
    --icon-grey: #b2b5b8;
    --paper: #ffffff;
    --backdrop: #e7e3dd;
  }
  * { margin: 0; padding: 0; box-sizing: border-box; }
  html, body {
    width: 1200px; height: 870px; overflow: hidden;
    background: var(--backdrop);
    font-family: "Exo 2", sans-serif;
  }
  .card {
    position: absolute; left: 380px; top: 50px;
    width: 440px; height: 770px;
    background: var(--paper);
    overflow: hidden;
    box-shadow: 0 6px 18px rgba(0,0,0,0.12);
  }
  .brand {
    position: absolute; top: 0; left: 0; width: 100%; height: 290px;
    display: flex; align-items: center; justify-content: center; gap: 16px;
  }
  .brand-mark {
    width: 34px; height: 34px; background: var(--navy);
  }
  .brand-name {
    font-size: 60px; font-weight: 600; line-height: 1;
    letter-spacing: 3px; color: var(--navy);
  }
  .name-band {
    position: absolute; top: 290px; left: 0; width: 100%; height: 118px;
    background: var(--navy); color: var(--paper);
    display: flex; flex-direction: column; justify-content: center; align-items: center;
  }
  .person-name { font-size: 36px; font-weight: 600; line-height: 1.1; }
  .person-title { font-size: 22px; font-weight: 400; letter-spacing: 0.5px; }
  .contacts { position: absolute; top: 465px; left: 0; width: 100%; }
  .contact-row {
    position: relative; height: 62px; margin-bottom: 16px;
  }
  .contact-icon {
    position: absolute; left: 40px; top: 0; width: 60px; height: 62px;
    background: var(--icon-grey);
    display: flex; align-items: center; justify-content: center;
  }
  .contact-bar {
    position: absolute; left: 110px; right: 0; top: -10px; height: 72px;
    background: var(--bar-grey); color: var(--navy);
    display: flex; flex-direction: column; justify-content: center;
    padding-left: 20px; font-size: 21px; line-height: 1.15; letter-spacing: 0.3px;
  }
  .card-footer-line {
    position: absolute; left: 0; bottom: 0; width: 100%; height: 8px; background: var(--navy);
  }
  .website-tab {
    position: absolute; bottom: 0; left: 70px; width: 300px; height: 56px;
    background: var(--navy); color: var(--paper);
    border-radius: 26px 26px 0 0;
    display: flex; align-items: center; justify-content: center;
    font-size: 22px; letter-spacing: 0.5px;
  }
</style>
</head>
<body>
  <div class="card">
    <div class="brand">
      <div class="brand-mark"></div>
      <div class="brand-name">PLM</div>
    </div>

    <div class="name-band">
      <div class="person-name">Daniel Marsh</div>
      <div class="person-title">Managing Director</div>
    </div>

    <div class="contacts">
      <div class="contact-row">
        <div class="contact-icon">
          <svg width="34" height="24" viewBox="0 0 34 24" aria-hidden="true">
            <rect x="1" y="1" width="32" height="22" fill="none" stroke="#fff" stroke-width="2"/>
            <polyline points="1,1 17,14 33,1" fill="none" stroke="#fff" stroke-width="2"/>
          </svg>
        </div>
        <div class="contact-bar">info@plmadvisory.com</div>
      </div>
      <div class="contact-row">
        <div class="contact-icon">
          <svg width="34" height="30" viewBox="0 0 34 30" aria-hidden="true">
            <path d="M2 10 Q17 0 32 10 L28 13 Q17 6 6 13 Z" fill="#fff"/>
            <rect x="7" y="14" width="20" height="14" rx="2" fill="#fff"/>
            <circle cx="17" cy="21" r="4" fill="#b2b5b8"/>
          </svg>
        </div>
        <div class="contact-bar">0044 5678 123</div>
      </div>
      <div class="contact-row">
        <div class="contact-icon">
          <svg width="34" height="30" viewBox="0 0 34 30" aria-hidden="true">
            <polygon points="17,2 33,15 29,15 29,28 5,28 5,15 1,15" fill="#fff"/>
            <rect x="14" y="18" width="6" height="10" fill="#b2b5b8"/>
          </svg>
        </div>
        <div class="contact-bar">
          <span>Harbor Office Suite 12</span>
          <span>Ave Linden, NJ 00000</span>
        </div>
      </div>
    </div>

    <div class="card-footer-line"></div>
    <div class="website-tab">www.plmadvisory.com</div>
  </div>
</body>
</html>
```